Logo and Business Card for Dental Office

We are opening a periodontal office (dental specialist for dental implants and gum diseases). It is a brand new state of the art facility with a focus on the most effective treatments for retaining natural teeth, or replacing teeth with implants when they must be lost. Strong emphasis on customer service and amenities for patient comfort. We are located just outside of Boston, MA.

Target Market(s)

potential adult patients, dentists in the community that will refer patients for specialized care

Industry/Entity Type

Dental

Requirements
Must have
• business name, address, phone number, website
Marcus T. Pellinger, DMD LLC
427 Corliss Street, Ste 305
Brookmere, NH 03999
603-555-0172
603-555-0148 Fax
DrPellinger.example

the uploaded file has a rough version of what I'm looking for in the logo, I like the colors but it can be varies some.
Nice to have
• simple logo or symbol on business card, one possible idea I had was an abstract symbol of a screw or threads that might represent a dental implant, the attached file gives an idea of where to start.
Should not have
• I want a professional feel, no cartoons of teeth that appear childish, etc
The font should be easy to read with no curly/swirly shapes.

```html
<!DOCTYPE html>
<html lang="en">
<head>
<meta charset="utf-8">
<title>Corliss Periodontal Studio — Stationery</title>
<link href="https://fonts.googleapis.com/css2?family=Cinzel:wght@400;600&display=swap" rel="stylesheet">
<style>
  :root {
    --navy: #002b55;
    --steel: #8fb0c8;
    --paper: #ffffff;
    --backdrop: #f2f2f2;
    --ghost: #f3f3f3;
  }
  * { margin: 0; padding: 0; box-sizing: border-box; }
  html, body { width: 1200px; height: 900px; overflow: hidden; }
  body {
    background: var(--backdrop);
    font-family: "Cinzel", "Times New Roman", serif;
    color: var(--navy);
    position: relative;
  }

  .brand { display: flex; align-items: center; gap: 8px; }
  .brand-dot { width: 14px; height: 14px; border-radius: 50%; background: var(--navy); flex: none; }
  .brand-name { font-size: 16px; font-weight: 600; color: var(--navy); letter-spacing: 0.3px; white-space: nowrap; }

  /* Business card — front */
  .card-front {
    position: absolute; left: 174px; top: 227px;
    width: 346px; height: 207px;
    background: var(--paper);
    display: flex; align-items: center; justify-content: center;
  }

  /* Business card — back */
  .card-back {
    position: absolute; left: 173px; top: 454px;
    width: 350px; height: 209px;
    background: var(--paper);
    overflow: hidden;
  }
  .card-back .name-band {
    height: 57px; background: var(--navy);
    color: #fff; font-size: 19px; letter-spacing: 0.6px;
    display: flex; align-items: center; justify-content: center;
  }
  .card-back .ghost-mark {
    position: absolute; left: 16px; top: 88px;
    width: 92px; height: 92px; border-radius: 50%;
    background: var(--ghost);
  }
  .card-back .contact {
    position: absolute; right: 41px; top: 88px;
    text-align: right; font-size: 12.5px; font-weight: 600; line-height: 17.5px;
    font-variant: small-caps; font-style: normal;
  }
  .card-back .contact .muted { color: var(--steel); font-weight: 400; }

  /* Letterhead */
  .letterhead {
    position: absolute; left: 576px; top: 110px;
    width: 485px; height: 626px;
    background: var(--paper);
  }
  .letterhead .header-band {
    height: 111px; background: var(--navy);
    display: flex; flex-direction: column; align-items: center;
    padding-top: 38px;
  }
  .letterhead .brand-dot { width: 20px; height: 20px; background: #fff; }
  .letterhead .brand-name { font-size: 24px; color: #fff; line-height: 28px; }
  .letterhead .practitioner {
    color: #fff; font-size: 12.5px; letter-spacing: 0.4px; margin-top: 26px; line-height: 15px;
  }
  .letterhead .footer {
    position: absolute; left: 0; right: 0; top: 558px;
    text-align: center; font-size: 13px; font-weight: 600; line-height: 19px;
    font-variant: small-caps;
  }
  .letterhead .footer span + span { margin-left: 14px; }
  .letterhead .footer .muted { color: var(--steel); font-weight: 400; }
</style>
</head>
<body>

  <section class="card-front">
    <div class="brand">
      <span class="brand-dot"></span>
      <span class="brand-name">Corliss Periodontal Studio</span>
    </div>
  </section>

  <section class="card-back">
    <div class="name-band">Marcus T. Pellinger, DMD LLC</div>
    <div class="ghost-mark"></div>
    <address class="contact">
      <div>427 Corliss Street, Ste 305</div>
      <div>Brookmere, NH 03999</div>
      <div class="muted">603-555-0172</div>
      <div>603-555-0148 Fax</div>
      <div class="muted">www.DrPellinger.example</div>
    </address>
  </section>

  <section class="letterhead">
    <header class="header-band">
      <div class="brand">
        <span class="brand-dot"></span>
        <span class="brand-name">Corliss Periodontal Studio</span>
      </div>
      <div class="practitioner">Marcus T. Pellinger, DMD LLC</div>
    </header>
    <footer class="footer">
      <div><span>427 Corliss Street, Ste 305</span><span class="muted">Brookmere, NH 03999</span></div>
      <div><span>603-555-0172</span><span class="muted">603-555-0148 Fax</span><span>www.DrPellinger.example</span></div>
    </footer>
  </section>

</body>
</html>
```